Velmora Interiors Stationary Set

Velmora Interiors is a bespoke interior design firm set to provide services to VIP clients with elegance and minimalism is the main theme for our stationary set. We require a full stationary set covering A4 letterhead, A4 & A3 envelopes, business cards, USB's, CDs, email signature and any other item the designer sees fit. logo is already designed and finalized, and we require the designer to use it as is without modifying the logo.

Address to be used on letterhead / business cards ...etc shall be as follows:

Phone : +971 2 518 3074
P.O. Box : 609318
Address: Block C&D, Bldg. 27, Court 14, Abu Dhabi, United Arab Emirates
Website: www.velmorainteriors-example.com

Target Market(s)

VIP Clients

Industry/Entity Type

Interior Design

Other font styles liked:
• something to be unique

Colors

Designer to choose colors to be used in the design.

Requirements
Must have
• Elegant, minimalistic
Nice to have
• Simple yet elegant design having a sharp yet clean cut format
Should not have
• No additional colours, just colours that are used in the logo (silver, black or gold)

```html
<!DOCTYPE html>
<html lang="en">
<head>
<meta charset="utf-8">
<title>Velmora Interiors Stationery Set</title>
<link href="https://fonts.googleapis.com/css2?family=Open+Sans:wght@400&family=Roboto:wght@300;400&display=swap" rel="stylesheet">
<style>
  :root{
    --backdrop:#62616d;
    --paper:#f7f7f8;
    --paper-shade:#ececee;
    --flap:#dcdcdf;
    --ink:#4a4a4f;
    --silver:#a9a9ad;
    --silver-faint:#e6e6e9;
    --rule:#b9b9bd;
    --signature-tone:#dedee1;
  }
  *{box-sizing:border-box;margin:0;padding:0}
  html,body{width:1200px;height:899px;overflow:hidden}
  body{
    background:var(--backdrop);position:relative;
    font-family:'Roboto',sans-serif;color:var(--ink);
    -webkit-font-smoothing:antialiased;-moz-osx-font-smoothing:grayscale;
    font-synthesis:none;
  }
  .brand{font-family:'Roboto',sans-serif;font-weight:300;color:var(--silver);letter-spacing:.04em;white-space:nowrap}
  .contact{list-style:none;font-family:'Roboto',sans-serif;color:var(--silver)}
  .contact li{display:flex;align-items:center;gap:3px;white-space:nowrap}
  .contact .dot{width:5px;height:5px;border-radius:50%;background:var(--silver);flex:none}

  /* envelope front */
  .envelope-front{position:absolute;left:203px;top:188px;width:404px;height:280px;overflow:hidden}
  .envelope-front .flap{position:absolute;left:0;top:0}
  .envelope-front .face{position:absolute;left:0;top:80px;width:404px;height:200px;background:var(--paper)}
  .envelope-front .brand-main{position:absolute;left:30px;top:118px;font-size:17px}
  .envelope-front .contact{position:absolute;left:30px;top:226px;font-size:5px;line-height:7px}
  .envelope-front .watermark{
    position:absolute;left:300px;top:100px;width:48px;height:156px;
    display:flex;align-items:center;justify-content:center;overflow:hidden;
  }
  .envelope-front .watermark span{
    writing-mode:vertical-rl;transform:rotate(180deg);
    font-size:38px;color:var(--silver-faint);letter-spacing:.02em;
  }

  /* envelope back */
  .envelope-back{position:absolute;left:202px;top:503px;width:402px;height:202px;background:var(--paper);overflow:hidden}
  .envelope-back svg{position:absolute;left:0;top:0}
  .envelope-back .brand-top{position:absolute;left:0;width:100%;top:28px;text-align:center;font-size:15px}
  .envelope-back .brand-corner{position:absolute;right:22px;bottom:26px;font-size:12px}
  .envelope-back .contact{position:absolute;left:26px;top:154px;font-size:4.4px;line-height:6.2px}
  .envelope-back .contact .dot{width:4px;height:4px}

  /* letterhead */
  .letterhead{position:absolute;left:650px;top:198px;width:390px;height:518px;background:var(--paper);font-family:'Open Sans',sans-serif;overflow:hidden}
  .letterhead .top-band{position:absolute;left:0;right:0;top:0;height:176px;background:var(--paper-shade)}
  .letterhead .bottom-band{position:absolute;left:0;right:0;top:351px;height:167px;background:var(--paper-shade)}
  .letterhead .brand{position:absolute;left:42px;top:50px;font-size:14px}
  .letterhead .contact-block{position:absolute;left:243px;top:39px;padding-left:8px;border-left:1px solid var(--rule)}
  .letterhead .contact{color:var(--ink);font-size:7px;line-height:9px}
  .letterhead .body{position:absolute;left:44px;top:128px;width:302px;font-size:6.6px;line-height:9.5px;color:var(--ink);text-align:justify}
  .letterhead .body p{margin-bottom:9.5px}
  .letterhead .signature{position:absolute;left:44px;top:376px;width:44px;height:40px;background:var(--signature-tone)}
  .letterhead .address{position:absolute;left:0;right:0;top:474px;display:flex;justify-content:center;align-items:center;gap:3px;font-family:'Roboto',sans-serif;font-size:7px;color:var(--ink);white-space:nowrap}
  .letterhead .address .dot{width:6px;height:6px;border-radius:50%;background:var(--silver)}
</style>
</head>
<body>

<section class="envelope-front" aria-label="Envelope front">
  <svg class="flap" width="404" height="80" viewBox="0 0 404 80">
    <path d="M12 0 H380 Q392 0 396 12 L404 80 H0 L6 12 Q8 0 12 0Z" fill="var(--flap)"/>
  </svg>
  <div class="face"></div>
  <div class="brand brand-main">Velmora Interiors</div>
  <div class="watermark brand" aria-hidden="true"><span>Velmora</span></div>
  <ul class="contact">
    <li><span class="dot"></span>+971 2 518 3074</li>
    <li><span class="dot"></span>info@velmorainteriors-example.com</li>
    <li><span class="dot"></span>www.velmorainteriors-example.com</li>
    <li><span class="dot"></span>Block C&amp;D, Bldg. 27, Court 14, Abu Dhabi, United Arab Emirates</li>
  </ul>
</section>

<section class="envelope-back" aria-label="Envelope back">
  <svg width="402" height="202" viewBox="0 0 402 202">
    <path d="M384 8 L362 74 Q358 82 348 82 H40 Q30 82 27 74 L0 0" fill="none" stroke="var(--flap)" stroke-width="1"/>
    <path d="M402 0 L384 202" stroke="var(--silver)" stroke-width=".6"/>
  </svg>
  <div class="brand brand-top">Velmora</div>
  <div class="brand brand-corner">Velmora Interiors</div>
  <ul class="contact">
    <li><span class="dot"></span>+971 2 518 3074</li>
    <li><span class="dot"></span>info@velmorainteriors-example.com</li>
    <li><span class="dot"></span>www.velmorainteriors-example.com</li>
    <li><span class="dot"></span>Block C&amp;D, Bldg. 27, Court 14, Abu Dhabi, United Arab Emirates</li>
  </ul>
</section>

<section class="letterhead" aria-label="Letterhead">
  <div class="top-band"></div>
  <div class="bottom-band"></div>
  <div class="brand">Velmora Interiors</div>
  <div class="contact-block">
    <ul class="contact">
      <li><span class="dot"></span>+971 2 518 3074</li>
      <li><span class="dot"></span>info@velmorainteriors-example.com</li>
      <li><span class="dot"></span>www.velmorainteriors-example.com</li>
    </ul>
  </div>
  <div class="body">
    <p>Dear customer,</p>
    <p>Lorem ipsum dolor sit amet, consectetur adipisicing elit, sed do eiusmod tempor incididunt ut labore et dolore magna aliqua. Ut enim ad minim veniam, quis nostrud exercitation ullamco laboris nisi ut aliquip ex ea commodo consequat. Duis aute irure dolor in reprehenderit in voluptate velit esse cillum dolore eu fugiat nulla pariatur. Excepteur sint occaecat cupidatat non proident, sunt in culpa qui officia deserunt mollit anim id est laborum.</p>
    <p>Lorem ipsum dolor sit amet, consectetur adipisicing elit, sed do eiusmod tempor incididunt ut labore et dolore magna aliqua. Ut enim ad minim veniam, quis nostrud exercitation ullamco laboris nisi ut aliquip ex ea commodo consequat. Duis aute irure dolor in reprehenderit in voluptate velit esse cillum dolore eu fugiat nulla pariatur. Excepteur sint occaecat cupidatat non proident, sunt in culpa qui officia deserunt mollit anim id est laborum.</p>
    <p>Lorem ipsum dolor sit amet, consectetur adipisicing elit, sed do eiusmod tempor incididunt ut labore et dolore magna aliqua. Ut enim ad minim veniam, quis nostrud exercitation ullamco laboris nisi ut aliquip ex ea commodo consequat. Duis aute irure dolor in reprehenderit in voluptate velit esse cillum dolore eu fugiat nulla pariatur. Excepteur sint occaecat cupidatat non proident, sunt in culpa qui officia deserunt mollit anim id est laborum.</p>
    <p>Lorem ipsum dolor sit amet, consectetur adipisicing elit, sed do eiusmod tempor incididunt ut labore et dolore magna aliqua. Ut enim ad minim veniam, quis nostrud exercitation ullamco laboris nisi ut aliquip ex ea commodo consequat. Duis aute irure dolor in reprehenderit.</p>
    <p>Yours Sincerely,</p>
  </div>
  <div class="signature" role="img" aria-label="Handwritten signature"></div>
  <div class="address"><span class="dot"></span>Block C&amp;D, Bldg. 27, Court 14, Abu Dhabi, United Arab Emirates</div>
</section>

</body>
</html>
```